Steadfast Valve Works

I need a business card with the attached logo.
The second page I have attached is what we are looking for. We want doubles sided. We would like the blues fading and the logo on the back.

Industry/Entity Type

Business

```html
<!DOCTYPE html>
<html lang="en">
<head>
<meta charset="UTF-8">
<title>Steadfast Valve Works – Business Card</title>
<link href="https://fonts.googleapis.com/css2?family=Open+Sans:wght@400;600;700&display=swap" rel="stylesheet">
<style>
  :root {
    --page-bg: #e6e8ec;
    --navy-deep: #0f2c5c;
    --navy: #1d4a86;
    --navy-mid: #2b5a98;
    --sky: #8db8e2;
    --sky-pale: #b9d5ef;
    --brand-blue: #1668b8;
    --white: #ffffff;
  }
  * { margin: 0; padding: 0; box-sizing: border-box; }
  html, body {
    width: 1200px;
    height: 1000px;
    overflow: hidden;
    background: var(--page-bg);
    font-family: "Open Sans", Arial, sans-serif;
  }
  .canvas {
    position: relative;
    width: 1200px;
    height: 1000px;
  }
  .card {
    position: absolute;
    width: 700px;
    height: 400px;
    box-shadow: 0 8px 22px rgba(0, 0, 0, 0.25);
    overflow: hidden;
  }
  /* Front side */
  .card-front {
    left: 80px;
    top: 60px;
    background: linear-gradient(180deg, var(--navy) 0%, var(--navy-mid) 35%, var(--navy-deep) 100%);
    display: flex;
    align-items: center;
    justify-content: center;
  }
  .front-brand {
    display: flex;
    align-items: center;
    gap: 16px;
  }
  .brand-square {
    width: 30px;
    height: 30px;
    background: var(--brand-blue);
  }
  .front-brand-name {
    font-size: 40px;
    font-weight: 700;
    letter-spacing: 2px;
    text-transform: uppercase;
    color: var(--brand-blue);
  }
  /* Back side */
  .card-back {
    left: 420px;
    top: 530px;
    background: linear-gradient(115deg, var(--navy) 0%, var(--navy-mid) 40%, var(--sky) 72%, var(--sky-pale) 100%);
    color: var(--white);
  }
  .person-name {
    position: absolute;
    left: 34px;
    top: 22px;
    font-size: 56px;
    font-weight: 600;
    letter-spacing: 2px;
    line-height: 1.1;
  }
  .person-role {
    position: absolute;
    left: 36px;
    top: 94px;
    font-size: 22px;
    font-weight: 400;
    text-transform: uppercase;
  }
  .contact-list {
    position: absolute;
    left: 36px;
    bottom: 26px;
    list-style: none;
  }
  .contact-item {
    display: flex;
    align-items: center;
    gap: 14px;
    font-size: 24px;
    height: 44px;
  }
  .contact-icon {
    width: 26px;
    height: 26px;
    fill: var(--white);
    flex: none;
  }
  .back-brand-name {
    position: absolute;
    right: 30px;
    bottom: 44px;
    font-size: 22px;
    font-weight: 700;
    letter-spacing: 1px;
    text-transform: uppercase;
    color: var(--brand-blue);
  }
</style>
</head>
<body>
<main class="canvas">
  <section class="card card-front" aria-label="Card front">
    <div class="front-brand">
      <span class="brand-square"></span>
      <span class="front-brand-name">Steadfast Valve Works</span>
    </div>
  </section>

  <section class="card card-back" aria-label="Card back">
    <h1 class="person-name">Name Surname</h1>
    <p class="person-role">Position</p>
    <ul class="contact-list">
      <li class="contact-item">
        <svg class="contact-icon" viewBox="0 0 24 24" aria-hidden="true">
          <path d="M3 8c0-2 2-4 9-4s9 2 9 4v2h-5V8H8v2H3z"/>
          <path d="M5 20l2-8h10l2 8z M12 13.5a2.5 2.5 0 1 0 0.01 0z"/>
        </svg>
        <span>000 0000</span>
      </li>
      <li class="contact-item">
        <svg class="contact-icon" viewBox="0 0 24 24" aria-hidden="true">
          <path d="M2 5h20v14H2z M4 7l8 6 8-6" fill="none" stroke="#ffffff" stroke-width="0"/>
          <path d="M2 5h20L12 13z"/>
          <path d="M2 7l10 8 10-8v12H2z"/>
        </svg>
        <span>email@steadfastvalve.com</span>
      </li>
      <li class="contact-item">
        <svg class="contact-icon" viewBox="0 0 24 24" aria-hidden="true">
          <path d="M12 2a7 7 0 0 0-7 7c0 5 7 13 7 13s7-8 7-13a7 7 0 0 0-7-7zm0 9.5a2.5 2.5 0 1 1 0-5 2.5 2.5 0 0 1 0 5z"/>
        </svg>
        <span>PO Box 0000</span>
      </li>
    </ul>
    <span class="back-brand-name">Steadfast Valve Works</span>
  </section>
</main>
</body>
</html>
```